Payroll Brochure

Create a brochure with the copy i have provided . A simple easy tp read brochure that shows wat we do we handle payroll taxes insurance 401k etc

```html
<!DOCTYPE html>
<html lang="en">
<head>
<meta charset="utf-8">
<title>VPC Payroll Brochure</title>
<link href="https://fonts.googleapis.com/css2?family=Source+Sans+3:wght@400;600&display=swap" rel="stylesheet">
<style>
  :root {
    --backdrop: #c0c0c0;
    --paper: #ffffff;
    --brand: #6d0f13;
    --accent: #7d1418;
    --ink: #222222;
    --pill-text: #ffffff;
  }
  * { margin: 0; padding: 0; box-sizing: border-box; }
  html, body {
    width: 1087px; height: 1200px; overflow: hidden;
    background: var(--backdrop);
    font-family: "Source Sans 3", "Myriad Pro", sans-serif;
    color: var(--ink);
  }
  .canvas { position: relative; width: 1087px; height: 1200px; }
  .page {
    position: absolute; left: 153.5px; width: 780px; height: 552px;
    background: var(--paper);
  }
  .page--inside { top: 33px; }
  .page--back { top: 600px; }

  .block { position: absolute; width: 342px; }
  .col-left { left: 171.5px; }
  .col-right { left: 561px; }

  .pill {
    display: inline-block;
    background: var(--brand);
    color: var(--pill-text);
    font-size: 10.6px;
    line-height: 17.5px;
    height: 17.5px;
    padding: 0 6.5px;
    border-radius: 9px;
    margin-bottom: 7px;
  }
  .item {
    font-size: 7.6px;
    line-height: 9.5px;
    margin-left: 7px;
    margin-bottom: 9.4px;
  }
  .item .label { color: var(--accent); }

  .hero-photo {
    position: absolute; left: 178.5px; top: 63.5px; width: 339.5px; height: 226.5px;
    background: linear-gradient(135deg, #8a8e92 0%, #b9a07c 35%, #a86a3c 60%, #d8cfc4 85%, #efece6 100%);
  }
  .brand-row {
    position: absolute; left: 195px; top: 322px; width: 320px;
    display: flex; align-items: center;
  }
  .brand-mark { display: flex; align-items: center; gap: 4px; color: var(--brand); font-size: 14px; font-weight: 600; }
  .brand-mark .square { width: 10px; height: 10px; background: var(--brand); }
  .brand-title { margin-left: 51px; color: var(--accent); font-size: 12px; }
  .lead-question {
    position: absolute; left: 178.5px; top: 353px; width: 341px;
    text-align: center; color: var(--accent); font-size: 11.6px;
  }
  .intro { position: absolute; left: 178.5px; top: 403px; width: 342px; }
  .intro .item { margin-left: 0; }

  .extras {
    position: absolute; left: 568.5px; top: 855px;
    font-size: 6.6px; line-height: 8.6px;
  }
</style>
</head>
<body>
<div class="canvas">
  <div class="page page--inside"></div>
  <div class="page page--back"></div>

  <div class="hero-photo" role="img" aria-label="Photo of a person typing on a laptop at a wooden desk with a coffee cup and paperwork"></div>

  <div class="brand-row">
    <div class="brand-mark"><span class="square"></span>VPC</div>
    <div class="brand-title">The VPC Advantage</div>
  </div>
  <div class="lead-question">What makes VPC uniquely qualified to be your service provider?</div>

  <div class="intro">
    <p class="item"><span class="label">People :</span> VPC has gone to great lengths to hire and train a world-class team of experienced payroll and HR professionals that are genuinely interested in making sure our clients receive the very best in service and support.</p>
    <p class="item"><span class="label">Process :</span> Developed over the years, the VPC process has been designed with speed and accuracy in mind. VPC does what’s needed to make sure our clients are presented with speedy responses to their questions, and produce accurate, reliable, and timely payrolls. With VPC’s custom designed software, we can easily tailor to your payroll needs.</p>
    <p class="item"><span class="label">Products :</span> VPC has developed a comprehensive suite of products and services that will fit your needs.</p>
    <p class="item"><span class="label">Flexibility :</span> VPC will design HR solutions that meet your specific needs and requirements.</p>
  </div>

  <section class="block col-right" style="top:59px">
    <h2 class="pill">Payroll and</h2>
    <p class="item"><span class="label">Flexible –</span> VPC’S flexible and powerful payroll module allows you the ability to grow you’re your business by meeting your unique needs. Supporting payrolls for very large to very small companies,</p>
    <p class="item"><span class="label">Efficient –</span> Get payroll done efficiently and accurately by relying on our flexible design to handle even the most complex payroll needs.</p>
    <p class="item"><span class="label">Grow without Growing Pains –</span> VPC’S technology and design is able to allow you to scale your business without adding all the incremental costs typically required.</p>
  </section>

  <section class="block col-right" style="top:173px">
    <h2 class="pill">Tax Reporting &amp; Payments</h2>
    <p class="item"><span class="label">Accurate –</span> all payroll taxes (federal, state, local) are calculated accurately. Additionally, we determine proper local tax jurisdictions based on the employee home and work addresses.</p>
    <p class="item"><span class="label">Complete –</span> Federal, State, and Local withholding taxes as well as State and Federal Unemployment taxes are provided. Tax payments are integrated into the Accounts Payable and General Ledger modules.</p>
  </section>

  <section class="block col-right" style="top:265px">
    <h2 class="pill">Human Resources</h2>
    <p class="item">With our online HR tools, you can empower yourself to take control of your human resource needs or let us do it.</p>
    <p class="item"><span class="label">Get Big Company Services –</span> by using our online tools in conjunction with your service team, you will have access to HR services only afforded by some of the largest companies.</p>
    <p class="item"><span class="label">Library –</span> our online document library lets you and employees create your own library of information accessible at any time. Employees can upload documents and forms that can be kept in history as long as needed.</p>
  </section>

  <section class="block col-right" style="top:398px">
    <h2 class="pill">Benefit Enrollment</h2>
    <p class="item"><span class="label">Easy and Quick Enrollment –</span> our intuitive user experience quickly walks employees through their benefit enrollment process and allows them to compare different plans and select those that best meet their life needs.</p>
    <p class="item"><span class="label">Flexible Benefit Plans and Easy Setup Options –</span> Offer your clients Fortune 500 benefit plans or administer their plans in an easy to use, yet flexible benefit administration module.</p>
    <p class="item"><span class="label">You Pick –</span> with our flexible contribution setup features, you can contribute in any manner to your employees’ benefits while the system automatically processes them through payroll</p>
  </section>

  <section class="block col-left" style="top:626px">
    <h2 class="pill">On Boarding</h2>
    <p class="item"><span class="label">Customize your On Boarding –</span> you can customize your on boarding experience to your hiring needs as well as provide multiple workflows for different employee types. The on boarding experience can be branded for you, providing a personalized experience for the employees.</p>
    <p class="item"><span class="label">Custom Document Management –</span> our custom document mapping feature lets you use your own forms and documents as part of the on boarding and hiring process. When these forms are completed – and electronically signed – they stay in history as long as needed.</p>
    <p class="item"><span class="label">Intuitive –</span> with a focus on the user experience, your employees will find it easy and quick to get on boarded with you.</p>
  </section>

  <section class="block col-left" style="top:763px">
    <h2 class="pill">Applicant Tracking</h2>
    <p class="item"><span class="label">Create and Post Jobs –</span> you can create jobs with just a few clicks and post them on all the popular job sites.</p>
    <p class="item"><span class="label">Hire the Right People –</span> by posting on popular job boards, as well as a proprietary database of job seekers, you will reach more candidates. You can choose to receive profiles of candidates that only match your background and specifications.</p>
    <p class="item"><span class="label">Manage the Hiring Process –</span> review candidates via video or online conferencing, review voice interviews, schedule in person interviews, have candidates answer certain online questions, and manage this entire process to find the right people. Once hired, they can be on boarded automatically.</p>
  </section>

  <section class="block col-left" style="top:904px">
    <h2 class="pill">Time and Attendance</h2>
    <p class="item"><span class="label">Make Time Entry Easy –</span> Simplify time tracking so you can spend less time on payroll tasks.</p>
    <p class="item"><span class="label">Everywhere Access –</span> Web interface, mobile apps, and on-premise time clocks allow employees to log their time wherever they are.</p>
    <p class="item"><span class="label">Plug and Play Time Clocks –</span> Time clocks are delivered ready-to-use with little or no setup required.</p>
  </section>

  <section class="block col-left" style="top:1008px">
    <h2 class="pill">ACA Compliance</h2>
    <p class="item"><span class="label">Client Tools –</span> provide you with reporting and analysis tools online so you can monitor ACA information and be proactive in managing your needs.</p>
    <p class="item"><span class="label">Affordability Test –</span> provide your with information about plan affordability with their employees so they can stay in compliance.</p>
    <p class="item"><span class="label">Large Employer Analysis –</span> analyze your control groups to determine if you will fall under the rules of</p>
  </section>

  <section class="block col-right" style="top:626px">
    <h2 class="pill">Self Service</h2>
    <p class="item"><span class="label">Manager –</span> your managers have access to their information via a highly intuitive online portal. Users can enter payroll time, create ad-hoc reports, preview and approve payroll and invoices, get invoice and check history, access employee records, communicate with employees, create, etc. Our single sign on allows managers that may have multiple business entities with VPC umbrella to use one login.</p>
    <p class="item"><span class="label">Employee –</span> employees can access pay information, request PTO, enroll in benefits, communicate with other employees, and access/change their personal information. They can also access corporate documents for review and upload personal documents as well.</p>
  </section>

  <section class="block col-right" style="top:738px">
    <h2 class="pill">WOTC</h2>
    <p class="item"><span class="label">Big Credits –</span> Work Opportunity Tax Credits (WOTC) allow you to receive between $2,400 and $9,600 for hiring eligible employees</p>
    <p class="item"><span class="label">Easy and Quick –</span> Employees complete a simple questionnaire to determine eligibility for WOTC. All of the necessary filing and reporting is handled for you and your client.</p>
    <p class="item"><span class="label">Integrated –</span> WOTC is integrated wherever you would enter a new employee – back office payroll, online on boarding, and applicant tracking to ensure all employees are being evaluated.</p>
  </section>

  <div class="extras">
    <p>Workers Compensation and Benefits</p>
    <p>Pay as you go Workers’ Compensation- Multiple carriers available</p>
    <p>Access to a Multiple Employer 401K</p>
    <p>Access to various voluntary benefits</p>
  </div>
</div>
</body>
</html>
```